Worrunga Contracting Pty Ltd.

We need a corporate brand/logo for a new company. The company is represented by Indigenous Australians in Western Australias far north West. The aea is the Kimberley. The work we are involved in is contracting our services to companies. Our services range from heavy earth working machinary to landscape rehabilitation including revegetation. Other services we provide are demolition, contaminated sites and water management. We are essentially a services provider for hire. We tender mostly for contracts wit hmining companies.

```html
<!DOCTYPE html>
<html lang="en">
<head>
<meta charset="utf-8">
<title>Worrunga Contracting Pty Ltd. – Business Cards</title>
<link href="https://fonts.googleapis.com/css2?family=Poppins:wght@400;500;600&display=swap" rel="stylesheet">
<style>
  :root {
    --backdrop: #d4d4d4;
    --card: #ffffff;
    --ink: #1c1c1c;
    --ochre: #e8801e;
    --ochre-soft: #f3b27a;
    --ochre-pale: #f9dcc0;
    --shadow: rgba(0, 0, 0, 0.18);
  }
  * { box-sizing: border-box; margin: 0; padding: 0; }
  html, body {
    width: 1200px;
    height: 961px;
    overflow: hidden;
    background: var(--backdrop);
    font-family: "Poppins", sans-serif;
    color: var(--ink);
  }
  .canvas {
    position: relative;
    width: 1200px;
    height: 961px;
  }
  .card {
    position: absolute;
    width: 525px;
    height: 300px;
    background: var(--card);
    overflow: hidden;
    box-shadow: 0 14px 30px var(--shadow);
  }
  .card--front { left: 600px; top: 110px; }
  .card--back { left: 75px; top: 540px; }

  .emblem-area {
    position: absolute;
    width: 300px;
    height: 300px;
    border-radius: 50%;
    background: radial-gradient(circle, var(--ochre) 0%, var(--ochre-soft) 55%, var(--ochre-pale) 100%);
  }
  .card--front .emblem-area { left: -80px; top: -150px; }
  .card--back .emblem-area { right: -60px; bottom: -150px; }

  .wordmark {
    position: absolute;
    right: 40px;
    top: 168px;
    text-align: right;
    font-weight: 500;
    color: var(--ink);
  }
  .wordmark__name {
    display: block;
    font-size: 38px;
    line-height: 1;
    letter-spacing: 0.5px;
  }
  .wordmark__suffix {
    display: block;
    margin-top: 8px;
    font-size: 12px;
    letter-spacing: 5px;
  }

  .contact {
    position: absolute;
    left: 38px;
    top: 38px;
  }
  .contact__name {
    font-size: 16px;
    font-weight: 600;
    letter-spacing: 0.5px;
    text-transform: uppercase;
    line-height: 1.3;
  }
  .contact__role {
    font-size: 12px;
    color: var(--ochre);
    padding-bottom: 5px;
    border-bottom: 2px solid var(--ochre);
    width: 120px;
  }
  .contact__address {
    margin-top: 10px;
    font-size: 11px;
    line-height: 1.45;
  }
  .contact__list {
    list-style: none;
    margin-top: 10px;
    font-size: 11px;
    line-height: 1.4;
  }
  .contact__item {
    display: flex;
    align-items: center;
    gap: 7px;
    margin-bottom: 3px;
  }
  .contact__icon {
    width: 13px;
    height: 13px;
    flex: none;
  }
</style>
</head>
<body>
<main class="canvas">

  <section class="card card--front" aria-label="Card front">
    <div class="emblem-area" role="img" aria-label="Brand emblem artwork in ochre and rust tones"></div>
    <div class="wordmark">
      <span class="wordmark__name">Worrunga</span>
      <span class="wordmark__suffix">CONTRACTING PTY LTD</span>
    </div>
  </section>

  <section class="card card--back" aria-label="Card back">
    <div class="contact">
      <p class="contact__name">Daniel R. Cooper</p>
      <p class="contact__role">Executive Director</p>
      <p class="contact__address">PO Box 418, Kununurra WA<br>6743, Australia</p>
      <ul class="contact__list">
        <li class="contact__item">
          <svg class="contact__icon" viewBox="0 0 14 14" aria-hidden="true">
            <circle cx="7" cy="7" r="7" fill="var(--ochre)"/>
            <path d="M4.6 3.6l1.3 1.6-.7.9c.5 1 1.3 1.8 2.3 2.3l.9-.7 1.6 1.3-.8 1.3C6.6 10 4 7.4 3.7 4.4z" fill="#fff"/>
          </svg>
          08-9168-0147
        </li>
        <li class="contact__item">
          <svg class="contact__icon" viewBox="0 0 14 14" aria-hidden="true">
            <circle cx="7" cy="7" r="7" fill="var(--ochre)"/>
            <rect x="3.5" y="4.5" width="7" height="5" fill="none" stroke="#fff" stroke-width="1"/>
            <path d="M3.5 4.5L7 7.3l3.5-2.8" fill="none" stroke="#fff" stroke-width="1"/>
          </svg>
          info@worrungamail.com
        </li>
        <li class="contact__item">
          <svg class="contact__icon" viewBox="0 0 14 14" aria-hidden="true">
            <circle cx="7" cy="7" r="7" fill="var(--ochre)"/>
            <circle cx="7" cy="7" r="3.6" fill="none" stroke="#fff" stroke-width="0.9"/>
            <ellipse cx="7" cy="7" rx="1.6" ry="3.6" fill="none" stroke="#fff" stroke-width="0.9"/>
            <path d="M3.4 7h7.2" stroke="#fff" stroke-width="0.9"/>
          </svg>
          www.worrungaweb.com
        </li>
      </ul>
    </div>
    <div class="emblem-area" role="img" aria-label="Brand emblem artwork in ochre and rust tones"></div>
  </section>

</main>
</body>
</html>
```